Business Card Design and Stationary design for consulting firm

Harbourline Sourcing are looking for a new business card design and a design for their A4 letterhead / A4 invoices.

We are seeking to heavily increase our brand awareness and require a business card that's professional in appearance but also shows flare and innovation. A card design that people will remember.

About Us
Harbourline Sourcing are `The Sourcing Crew’.
Our mission is to be one of Australia’s greatest companies. Our aim is to help our customers achieve the best result from their purchasing experience.

Our Requirement:
• IMPACT! IMPACT! IMPACT!
• BUSINESS & PROFESSIONAL LOOKING

• Our business colours are orange, blue and green (See the logo attached).

We have provided an Art Design specification (attached) that needs to be followed for you to win the design. This also has the font, which is used on the logo.

We are after a two sided business card

Side One should have the:
The company Logo
The Sourcing Crew
www.harbourlinesourcing.com.au
Procure | Personnel | Probity & Privacy
Sydney | Melbourne | Adelaide | Brisbane

Side Two
Logo (optional)
Harbourline Sourcing (optional)
Employee details (details listed below)

The above format is our preferred option, but if you think you can come up with something better, feel free to put it forward.

We are leaving the design up to you, but it must incorporate the logo.

We will need a template that we can change the employee details on, as we will be adding more staff over the coming months.

The details below are for one employee per card with the same design.
------------------------

Employee Details:

Marcus Del Arroyo MBA, MMgmtStratProc
Principal Consultant
0491 372 618
Marcus@harbourlinesourcing.com.au

Brianna Tolley
Consulting Manager
0462 915 308
Brianna@harbourlinesourcing.com.au

Our website is www.harbourlinesourcing.com.au

The Letterhead / invoice needs to incorporate:
the company Logo
The Sourcing Crew
Sydney | Melbourne | Adelaide | Brisbane but otherwise the design is over to you.

This file needs to be delivered in word format as other detail will be added to the documents.

We look forward to you award winning designs. If you require any further information please feel free to contact us.

Regards
Harbourline Sourcing

Target Market(s)

Our Target market is companies with 80+ employees. The market we segment is heavily male based, between the ages of 35-55 years of age.

Industry/Entity Type

Consulting

Contact Information for Business Card

See Project Description

Font styles to use
Other font styles liked:
• See Art Specification

Requirements
Must have
• Company Colours, See Project Description
Should not have
• Be outside the Art specification guidelines

```html
<!DOCTYPE html>
<html lang="en">
<head>
<meta charset="utf-8">
<title>Harbourline Sourcing – Business Card</title>
<link rel="stylesheet" href="https://fonts.googleapis.com/css2?family=Archivo+Narrow:wght@600;700&family=Oswald:wght@500&family=Montserrat:wght@700&display=swap">
<style>
  :root {
    --page: #e8e5e1;
    --card: #ffffff;
    --red: #c0171c;
    --blue: #2f5ecb;
    --green: #4b7b35;
    --ink: #111111;
    --brand-ink: #3a3f44;
    --white: #ffffff;
  }
  * { margin: 0; padding: 0; box-sizing: border-box; }
  html, body {
    width: 1200px; height: 1000px; overflow: hidden;
    background: var(--page);
  }
  .canvas { position: relative; width: 1200px; height: 1000px; }

  .card {
    position: absolute; width: 698px; height: 395px;
    background: var(--card);
    box-shadow: 4px 5px 8px rgba(0,0,0,.28);
    overflow: hidden;
  }
  .card--front { left: 69px; top: 92px; }
  .card--back { left: 418px; top: 522px; }

  .brand-name {
    position: absolute;
    font-family: "Montserrat", sans-serif; font-weight: 700;
    color: var(--brand-ink); letter-spacing: 1px; line-height: 1.05;
    display: flex; align-items: center; gap: 10px;
  }
  .brand-name .brand-dot {
    width: 16px; height: 16px; border-radius: 50%; background: var(--brand-ink); flex: none;
  }
  .card--front .brand-name { left: 28px; top: 110px; font-size: 21px; }
  .card--back .brand-name {
    left: 0; right: 0; top: 190px; justify-content: center; font-size: 26px;
  }

  .small-caps {
    font-family: "Archivo Narrow", sans-serif; font-weight: 700;
    font-variant: small-caps; color: var(--white);
  }

  .ribbon {
    position: absolute; right: 0;
    display: flex; flex-direction: column; justify-content: center; align-items: flex-end;
    padding-right: 12px;
    clip-path: polygon(22px 0, 100% 0, 100% 100%, 0 100%);
    box-shadow: 0 3px 4px rgba(0,0,0,.25);
  }
  .ribbon--name { top: 170px; left: 234px; height: 41px; background: var(--red); font-size: 21px; letter-spacing: 1px; }
  .ribbon--role { top: 221px; left: 271px; height: 37px; background: var(--blue); font-size: 20px; letter-spacing: 1.5px; }
  .ribbon--contact { top: 268px; left: 307px; height: 55px; background: var(--green); gap: 2px; }
  .contact-line { display: flex; align-items: center; gap: 10px; }
  .contact-line--phone { font-size: 17px; letter-spacing: 1px; }
  .contact-line--email { font-size: 14px; letter-spacing: .5px; }
  .contact-icon { width: 16px; height: 16px; flex: none; }

  .service-line {
    position: absolute; left: 0; right: 0; top: 364px; text-align: center;
    font-family: "Archivo Narrow", sans-serif; font-weight: 700; font-variant: small-caps;
    color: var(--ink); font-size: 17px; letter-spacing: 4px; word-spacing: 6px;
  }

  .band {
    position: absolute; left: 0; right: 0; text-align: center; color: var(--white);
  }
  .band--tagline {
    top: 256px; height: 37px; background: var(--red);
    font-family: "Oswald", sans-serif; font-weight: 500; font-size: 24px;
    letter-spacing: 6px; line-height: 37px; text-transform: uppercase;
  }
  .band--web {
    top: 299px; height: 36px; background: var(--green);
    font-family: "Oswald", sans-serif; font-weight: 500; font-size: 20px;
    letter-spacing: 1px; line-height: 36px; text-transform: uppercase;
  }
  .band--locations {
    top: 341px; height: 54px; background: var(--blue);
    display: flex; flex-direction: column; justify-content: center;
    font-size: 16px; letter-spacing: 1px; line-height: 24px;
  }
</style>
</head>
<body>
<div class="canvas">

  <section class="card card--front" aria-label="Business card front">
    <div class="brand-name"><span class="brand-dot"></span><span>HARBOURLINE<br>SOURCING</span></div>

    <div class="ribbon ribbon--name small-caps">Marcus Del Arroyo MBA, MMgmtStratProc</div>
    <div class="ribbon ribbon--role small-caps">Principal Consultant</div>
    <div class="ribbon ribbon--contact small-caps">
      <div class="contact-line contact-line--phone">0491 372 618
        <svg class="contact-icon" viewBox="0 0 16 16" aria-hidden="true">
          <circle cx="8" cy="8" r="7" fill="none" stroke="#fff" stroke-width="1.2"/>
          <path d="M5.3 4.3l1.3 1.6-.7 1c.5 1 1.2 1.7 2.2 2.2l1-.7 1.6 1.3-.8 1.2c-2.6-.3-4.6-2.3-4.9-4.9z" fill="#fff"/>
        </svg>
      </div>
      <div class="contact-line contact-line--email">Marcus@harbourlinesourcing.com.au
        <svg class="contact-icon" viewBox="0 0 16 16" aria-hidden="true">
          <circle cx="8" cy="8" r="7" fill="none" stroke="#fff" stroke-width="1.2"/>
          <rect x="4.3" y="5.5" width="7.4" height="5" fill="none" stroke="#fff" stroke-width="1"/>
          <path d="M4.3 5.5L8 8.5l3.7-3" fill="none" stroke="#fff" stroke-width="1"/>
        </svg>
      </div>
    </div>

    <p class="service-line">Procure | Personnel | Probity &amp; Privacy</p>
  </section>

  <section class="card card--back" aria-label="Business card back">
    <div class="brand-name"><span class="brand-dot"></span><span>HARBOURLINE SOURCING</span></div>

    <div class="band band--tagline">The Sourcing Crew</div>
    <div class="band band--web">www.harbourlinesourcing.com.au</div>
    <div class="band band--locations small-caps">
      <span>Procure | Personnel | Probity &amp; Privacy Sydney</span>
      <span>Melbourne | Adelaide | Brisbane</span>
    </div>
  </section>

</div>
</body>
</html>
```